Brisbane IT support business needs our first website

Hi All,

We are after a new website design for our IT solutions and support business.The business name is Kestrel Harbour Computing Services, or KHCS for short. We provide a range of solutions and services within the IT space.

I would like to utilize the two colours in our business logo I have uploaded.

I understand this is initially for the design only aspect of the site, but I would like to engage the winner to finish coding the website and finalize after also.

Target Market(s)

Other businesses owners and home users.

Industry/Entity Type

Business

Requirements
Must have
• Nice clean and functional design utilizing our business colours from the logo.

```html
<!DOCTYPE html>
<html lang="en">
<head>
<meta charset="utf-8">
<title>Kestrel Harbour Computing Services</title>
<link rel="stylesheet" href="https://fonts.googleapis.com/css2?family=Open+Sans:wght@300;400;600;700&display=swap">
<style>
  :root {
    --navy: #0b3b52;
    --navy-deep: #082e40;
    --orange: #e8771e;
    --orange-light: #f39a2c;
    --orange-btn: #e2691a;
    --ring: #cdc9c2;
    --teal: #3d7d8e;
    --paper: #efefef;
    --header: #ececec;
    --ink: #2c2c2c;
    --muted: #8d8d8d;
    --white: #ffffff;
  }
  * { margin: 0; padding: 0; box-sizing: border-box; }
  html, body { width: 1200px; height: 2316px; overflow: hidden; }
  body { position: relative; background: var(--white); font-family: "Open Sans", Arial, sans-serif; color: var(--ink); }
  .abs { position: absolute; }

  /* header */
  .site-header { left: 0; top: 0; width: 1200px; height: 143px; background: var(--header); }
  .brand { left: 116px; top: 28px; display: flex; align-items: center; gap: 16px; }
  .brand-mark { width: 78px; height: 78px; border-radius: 50%; background: var(--navy); }
  .brand-name { font-size: 52px; font-weight: 700; color: var(--orange); letter-spacing: 2px; }
  .call { left: 880px; top: 34px; display: flex; align-items: center; gap: 10px; }
  .call-text { line-height: 1.05; }
  .call-label { font-size: 25px; font-weight: 600; color: var(--orange); }
  .call-number { font-size: 25px; font-weight: 700; color: var(--navy); }

  /* hero */
  .hero { left: 0; top: 143px; width: 1200px; height: 527px; background: var(--navy); }
  .main-nav { left: 99px; top: 120px; width: 1002px; height: 59px; display: flex;
    background: linear-gradient(#f6a22f, #e9791c); }
  .main-nav a { flex: 1; display: flex; align-items: center; justify-content: center;
    color: var(--white); font-size: 12px; font-weight: 600; text-decoration: none; letter-spacing: .5px;
    border-right: 1px solid rgba(255,255,255,.25); }
  .main-nav a:last-child { border-right: 0; }
  .hero-photo { left: 99px; top: 179px; width: 1002px; height: 379px;
    background: linear-gradient(100deg, #8fa8bd 0%, #c9c3ba 30%, #e8e3dc 50%, #5d6a76 75%, #23303d 100%); }
  .slider-dots { left: 560px; top: 535px; display: flex; gap: 6px; }
  .slider-dots span { width: 18px; height: 18px; border-radius: 50%; background: var(--white); }
  .slider-dots span.on { background: var(--orange); }
  .hero-caption { left: 99px; top: 558px; width: 1002px; height: 57px; background: var(--paper);
    display: flex; align-items: center; justify-content: center; font-size: 27px; font-weight: 400; color: var(--ink); }

  /* tools */
  .tools-title { left: 0; top: 706px; width: 1200px; text-align: center; font-size: 35px; font-weight: 300;
    line-height: 1.22; color: #444; }
  .tool { top: 827px; width: 232px; height: 232px; border-radius: 50%; border: 42px solid var(--ring);
    background: var(--white); display: flex; align-items: center; justify-content: center; }

  /* welcome */
  .welcome { left: 0; top: 1130px; width: 1200px; height: 495px; background: var(--paper); }
  .hello { left: 99px; top: 1172px; font-size: 50px; font-weight: 600; color: var(--orange); line-height: 1.1; }
  .welcome-title { left: 99px; top: 1225px; font-size: 48px; font-weight: 300; color: #222; line-height: 1.1; }
  .welcome-sub { left: 99px; top: 1314px; font-size: 25px; font-weight: 400; color: var(--orange); white-space: nowrap; }
  .welcome-copy { left: 99px; width: 650px; font-family: Arial, sans-serif; font-size: 13.5px; line-height: 21px; color: var(--muted); }
  .why-title { left: 785px; top: 1188px; font-size: 34px; font-weight: 600; color: #111; }
  .why-list { left: 785px; top: 1256px; width: 320px; list-style: none; }
  .why-list li { position: relative; padding-left: 34px; font-size: 15px; color: var(--muted); line-height: 20px; margin-bottom: 19px; }
  .why-list li::before { content: ""; position: absolute; left: 0; top: 4px; width: 12px; height: 12px; background: var(--orange); }

  /* features */
  .feature { top: 1638px; width: 360px; text-align: center; }
  .feature-icon { width: 158px; height: 158px; margin: 0 auto; border-radius: 50%; background: var(--orange-light);
    display: flex; align-items: center; justify-content: center; }
  .feature-title { margin-top: 52px; font-size: 34px; font-weight: 300; line-height: 1.12; color: #333; }
  .feature-title strong { display: block; font-weight: 600; color: var(--orange); }
  .feature-copy { margin: 22px auto 0; width: 290px; font-family: Arial, sans-serif; font-size: 13.5px; line-height: 21px; color: var(--muted); }
  .more { display: inline-block; margin-top: 22px; width: 93px; height: 34px; line-height: 34px; background: var(--orange-btn);
    color: var(--white); font-size: 14px; font-weight: 700; text-decoration: none; }

  /* footer */
  .site-footer { left: 0; top: 2172px; width: 1200px; height: 144px; background: var(--navy-deep); }
  .social { left: 458px; top: 2202px; display: flex; gap: 30px; }
  .social span { width: 36px; height: 36px; border-radius: 50%; background: var(--white); }
  .copyright { left: 99px; top: 2268px; font-size: 15px; color: var(--white); }
</style>
</head>
<body>

<header class="abs site-header">
  <div class="abs brand">
    <span class="brand-mark"></span>
    <span class="brand-name">KHCS</span>
  </div>
  <div class="abs call">
    <svg width="40" height="42" viewBox="0 0 24 24"><path fill="#0b3b52" d="M6.6 10.8a15.1 15.1 0 0 0 6.6 6.6l2.2-2.2c.3-.3.7-.4 1-.2 1.1.4 2.3.6 3.6.6.6 0 1 .4 1 1V20c0 .6-.4 1-1 1A17 17 0 0 1 3 4c0-.6.4-1 1-1h3.5c.6 0 1 .4 1 1 0 1.3.2 2.5.6 3.6.1.3 0 .7-.2 1z"/></svg>
    <div class="call-text">
      <div class="call-label">Call Us:</div>
      <div class="call-number">555 0142 3386</div>
    </div>
  </div>
</header>

<section class="abs hero"></section>
<nav class="abs main-nav">
  <a href="#">HOME</a><a href="#">ABOUT</a><a href="#">BLOG</a><a href="#">SERVICES</a><a href="#">PRODUCTS</a><a href="#">CONTACTS</a>
</nav>
<div class="abs hero-photo" role="img" aria-label="Photo of smiling business colleagues talking around a meeting table in a bright office"></div>
<div class="abs slider-dots"><span class="on"></span><span></span><span></span></div>
<div class="abs hero-caption">BUILDING YOUR BUSINESS GROWTH &amp; PROSPERITY</div>

<h2 class="abs tools-title">USING BEST PRACTICE TOOLS TO<br>BUILD A BETTER BUSINESS</h2>

<div class="abs tool" style="left:101px">
  <svg width="84" height="84" viewBox="0 0 64 64"><path fill="#3d7d8e" d="M4 10 60 30 22 36z"/><path fill="#2b5d6b" d="M22 36 60 30 30 60z"/></svg>
</div>
<div class="abs tool" style="left:356px">
  <svg width="84" height="84" viewBox="0 0 64 64"><g fill="#3d7d8e"><path d="M10 50 42 18l4 4-32 32z"/><circle cx="48" cy="14" r="10"/><path d="M16 8l10 10-6 6L10 14z"/><path d="M24 28l6-6 26 26-6 6z"/></g><circle cx="48" cy="14" r="5" fill="#fff"/></svg>
</div>
<div class="abs tool" style="left:610px">
  <svg width="70" height="88" viewBox="0 0 48 64"><path fill="#333" d="M24 2a20 20 0 0 0-12 36c2 2 3 5 3 8h18c0-3 1-6 3-8A20 20 0 0 0 24 2z"/><rect x="15" y="49" width="18" height="4" fill="#333"/><rect x="16" y="55" width="16" height="4" fill="#333"/><rect x="19" y="60" width="10" height="3" fill="#333"/><path d="M18 20l6 22 6-22" stroke="#fff" stroke-width="2" fill="none"/></svg>
</div>
<div class="abs tool" style="left:865px">
  <svg width="84" height="84" viewBox="0 0 64 64"><g fill="none" stroke="#b3561d" stroke-width="5"><circle cx="32" cy="36" r="20"/><path d="M32 24v12h9M18 58l4-6M46 58l-4-6"/></g><circle cx="14" cy="14" r="8" fill="#b3561d"/><circle cx="50" cy="14" r="8" fill="#b3561d"/></svg>
</div>

<section class="abs welcome"></section>
<h2 class="abs hello">HELLO THERE!</h2>
<h2 class="abs welcome-title">WELCOME TO OUR SITE</h2>
<h3 class="abs welcome-sub">VESTIBULUM NEQUE EST, VARIUS IN CONDIMENTUM</h3>
<p class="abs welcome-copy" style="top:1362px">Praesent vestibulum molestie nonumm erit mais. Phasellu por fusce smium soina penati et manirtu rienntes nasetur memo leste lacuanulla dui. Fusce feug male suada odio. Morbi nuncod gridem dolore aecenas. Lorem ip dolor sit amet consectet adipiscing fermentum dictector. Aenean auctor wisi et urna liquat volutpapis rutrum ante.</p>
<p class="abs welcome-copy" style="top:1478px">Phasellu por fusce smium soina penati et manirtu rienntes nasetur memo lestie lacuanulla dui. Fusce feug male suada odio. Morbi nuncod gridem dolore aecenas. Lorem ip dolor sit amet consectet adipiscing fermentum dictector. Aenean auctor wisi et urna liquat volutpapis rutrum ante eu lacuestibulumlibero nisi porta vel scelerisque eget malesat neque. Etiam ursus leo vel metus ulla facilisi enean nec eros.</p>
<h2 class="abs why-title">WHY CHOOSE US</h2>
<ul class="abs why-list">
  <li>VESTIBULUM IACULIS LACINIA EST SEREN</li>
  <li>PROIN DICTUM ELEMENTU ATR</li>
  <li>FUSCE EUISMOD CONSEQUAT ANTE</li>
  <li>LOREM IPSUM DOLOR SIT LO</li>
  <li>AMCONSECTETUER ADIPISCING ELIT</li>
  <li>VIVAMUS VEL EROS EGET</li>
  <li>ALIQUAM CONGUE FERMENTUM NISL</li>
  <li>MAURIS ACCUMSAN NULLA VE</li>
</ul>

<div class="abs feature" style="left:62px">
  <div class="feature-icon"><svg width="76" height="76" viewBox="0 0 64 64" fill="#fff"><rect x="6" y="28" width="12" height="28" rx="2"/><path d="M22 56V30l10-18c2-4 8-3 8 2v10h14c3 0 5 3 4 6l-5 21c-1 3-3 5-6 5z"/></svg></div>
  <h3 class="feature-title"><strong>SUCCESSFUL</strong>PROJECTS</h3>
  <p class="feature-copy">Vivamus vel eros eget magna volutpat sagittis. Nulla faucibus nibh a magna tincidunt accumsan hendrerit nunc facilisis. Curabitur et libero sit amet ante hendrerit molestie. Cras a erat in leo</p>
  <a class="more" href="#">MORE</a>
</div>
<div class="abs feature" style="left:414px">
  <div class="feature-icon"><svg width="72" height="72" viewBox="0 0 24 24"><path fill="#fff" d="M6.6 10.8a15.1 15.1 0 0 0 6.6 6.6l2.2-2.2c.3-.3.7-.4 1-.2 1.1.4 2.3.6 3.6.6.6 0 1 .4 1 1V20c0 .6-.4 1-1 1A17 17 0 0 1 3 4c0-.6.4-1 1-1h3.5c.6 0 1 .4 1 1 0 1.3.2 2.5.6 3.6.1.3 0 .7-.2 1z"/></svg></div>
  <h3 class="feature-title"><strong>24/7 CLIENT</strong>SUPPORT</h3>
  <p class="feature-copy">Vivamus vel eros eget magna volutpat sagittis. Nulla faucibus nibh a magna tincidunt accumsan hendrerit nunc facilisis. Curabitur et libero sit amet ante hendrerit molestie. Cras a erat in leo</p>
  <a class="more" href="#">MORE</a>
</div>
<div class="abs feature" style="left:772px">
  <div class="feature-icon"><svg width="80" height="80" viewBox="0 0 64 64"><path fill="none" stroke="#fff" stroke-width="11" stroke-linecap="square" d="M12 34l14 14 26-30"/></svg></div>
  <h3 class="feature-title"><strong>SATISFACTION</strong>GUARANTEE</h3>
  <p class="feature-copy">Vivamus vel eros eget magna volutpat sagittis. Nulla faucibus nibh a magna tincidunt accumsan hendrerit nunc facilisis. Curabitur et libero sit amet ante hendrerit molestie. Cras a erat in leo</p>
  <a class="more" href="#">MORE</a>
</div>

<footer class="abs site-footer"></footer>
<div class="abs social"><span></span><span></span><span></span><span></span><span></span></div>
<p class="abs copyright">Copyright Tallowood Lawns 2014. All Rights Reserved.</p>

</body>
</html>
```